Homepage for the lumo-pathe Web Application

At the end of this text, you will find a link to a website that is under construction for a webApp that I intend to launch soon. The contest goal is for you to make redesign the homepage in a nice, fresh, modern Style. Only design, no coding necessary. It needs to have a responsive version for small screens like smart phones. Attached is the text for it, and some images that you may use. You are welcome to find or create additional supporting images. You can use PixaVendor.example or similar service to find new images as long as I can purchase the non-exclusive use rights for the images at similar prices. The contest is just for the home page. However, the winner, if I like the work and we can agree on a fair price, could be contracted on a one-on-one basis to do the rest of the site. You are welcome to suggest minor changes like font sizes and minor variations on the Header banner, but that banner is consistent with the user interface of the application therefore should not change too much. The information should flow somewhat continually without much use of side bars or things like that.
https://www.lumo-pathe.example
Sincerely,
Marek D. Holloway

```html
<!DOCTYPE html>
<html lang="en">
<head>
<meta charset="utf-8">
<title>Lumo Pathe — Find that document or item instantly</title>
<link href="https://fonts.googleapis.com/css2?family=Roboto:wght@400;500;700&display=swap" rel="stylesheet">
<style>
:root{
  --teal:#40c3c8;
  --teal-dark:#1f8fa3;
  --mint:#e8fdfb;
  --coral:#ff7f5a;
  --coral-btn:#ff8059;
  --ink:#2b2b2b;
  --white:#ffffff;
  --field:#e9fdfc;
  --star:#f5f542;
  --bullet:#e6f24a;
}
*{margin:0;padding:0;box-sizing:border-box}
html,body{width:1200px;height:2887px;overflow:hidden}
body{font-family:"Roboto",sans-serif;background:var(--coral);position:relative}
.abs{position:absolute}

/* header */
.site-header{position:absolute;left:0;top:0;width:1200px;height:242px;background:var(--teal)}
.brand{position:absolute;left:75px;top:76px;display:flex;align-items:center;gap:6px;color:var(--white);font-size:24px;font-weight:500;letter-spacing:1.5px}
.brand-dot{width:30px;height:30px;border-radius:50%;background:#ff9d84}
.field{position:absolute;top:67px;height:51px;width:210px;background:var(--field);border-radius:3px;color:#3a4a4c;font-size:18px;display:flex;align-items:center;justify-content:center}
.field.user{left:459px}
.field.pass{left:716px}
.login{position:absolute;left:966px;top:67px;width:144px;height:51px;border:2px solid var(--white);border-radius:4px;color:var(--white);font-size:20px;display:flex;align-items:center;justify-content:center}
.main-nav a{position:absolute;top:186px;color:var(--white);font-size:17px;text-decoration:none}

/* hero */
.hero{position:absolute;left:0;top:242px;width:1200px;height:700px;background:var(--mint)}
.hero-title{position:absolute;left:131px;top:383px;font-size:38px;font-weight:700;line-height:44px;color:var(--ink)}
.hero-copy{position:absolute;left:131px;top:497px;width:350px;font-size:22px;line-height:29px;color:#1d1d1d}
.btn-trial{position:absolute;left:131px;top:678px;width:268px;height:64px;background:var(--coral-btn);border-radius:8px;color:var(--white);font-size:22px;font-weight:500;display:flex;align-items:center;justify-content:center}
.hero-art{position:absolute;left:616px;top:358px;width:444px;height:454px;border-radius:20px;background:linear-gradient(150deg,#9ae6ea,#3bbcc4 60%,#1f8fa3)}

/* why storage */
.why-storage{position:absolute;left:0;top:902px;width:1200px;height:1209px;background:var(--teal);border-top-left-radius:62px;color:var(--white)}
.why-title{position:absolute;left:487px;top:1006px;font-size:40px;font-weight:700;line-height:44px;letter-spacing:.5px}
.sub{position:absolute;left:486px;font-size:20px;font-weight:500}
.sub.paper{top:1128px}
.sub.objects{top:1396px;left:485px}
.paper-copy{position:absolute;left:485px;top:1166px;width:545px;font-size:16.5px;line-height:26.7px}
.object-list{position:absolute;left:485px;top:1437px;width:545px;list-style:none;font-size:16.5px;line-height:29.2px}
.object-list li{position:relative}
.object-list li.dot::before{content:"";position:absolute;left:-24px;top:9px;width:11px;height:11px;border:1.6px solid var(--bullet);border-radius:50%}
.object-list b{font-weight:500}
.phone-art{position:absolute;left:106px;top:1221px;width:247px;height:487px;border-radius:26px;background:linear-gradient(160deg,#d6f7f8,#8ddfe3 55%,#2a9fb0)}

/* why brand */
.why-brand{position:absolute;left:0;top:2111px;width:1200px;height:776px;background:var(--coral);color:var(--white)}
.brand-title{position:absolute;left:373px;top:2214px;font-size:51px;font-weight:700}
.perks{position:absolute;left:373px;top:2303px;list-style:none;font-size:21px;font-weight:500}
.perks li{height:50px;display:flex;align-items:center;gap:14px}
.perks svg{flex:none}
.btn-trial-light{position:absolute;left:373px;top:2668px;width:360px;height:69px;background:var(--white);border-radius:8px;color:var(--coral);font-size:27px;font-weight:700;display:flex;align-items:center;justify-content:center}
</style>
</head>
<body>

<header class="site-header">
  <div class="brand"><span class="brand-dot"></span>Lumo Pathe</div>
  <div class="field user">User Name</div>
  <div class="field pass">Password</div>
  <div class="login">Login</div>
  <nav class="main-nav">
    <a style="left:385px">About</a>
    <a style="left:467px">Pricing</a>
    <a style="left:560px">Blog</a>
    <a style="left:628px">FAQs</a>
    <a style="left:703px">Support</a>
    <a style="left:802px">Reviews</a>
    <a style="left:904px">Contact Us</a>
    <a style="left:1031px">Free Trial</a>
  </nav>
</header>

<section class="hero"></section>
<h1 class="hero-title">Find that document<br>or item instantly.</h1>
<p class="hero-copy">Lumo-Pathe allows you to quickly find any file on your compute. Keeping track of all your paper documents and other belongings has never been easier.</p>
<div class="btn-trial">30 Day Free Trial</div>
<div class="hero-art" role="img" aria-label="Isometric illustration of a laptop whose screen is a filing cabinet, with a businessman pulling an orange folder from a drawer"></div>

<section class="why-storage"></section>
<div class="phone-art" role="img" aria-label="Isometric illustration of a smartphone showing folders holding items such as a wine bottle, a disc, a key and books"></div>
<h2 class="why-title abs" style="color:var(--white)">Why use a storage management<br>system like Lumo-Pathe?</h2>
<h3 class="sub paper" style="color:var(--white)">Managing paper documents</h3>
<p class="paper-copy" style="color:var(--white)">Most people and businesses have a variety of documents that need to be filed .As time passes, you might have a difficult time recalling what criterion you used to file your documents, making it hard to find that document with ease.<br>A storage management system like Lumo-Pathe allows any authorized user to instantly find any document regardless of who file it or which criterion was used.</p>
<h3 class="sub objects" style="color:var(--white)">Managing any non-document objects</h3>
<ul class="object-list" style="color:var(--white)">
  <li class="dot"><b>Storage boxes, closets, warehouses, and shelves</b>: Anything that you put away in storage, would better be indexed with a system that lets you find what you’re looking for instantly.</li>
  <li class="dot"><b>Books</b>: Whether you keep your books on display on shelves, or stored in boxes, you should keep them indexed if you ever want to find any of them in the future.</li>
  <li class="dot"><b>Wines:</b> Keeping your wines indexed on our system would prove invaluable in selecting and locating a wine bottle for any moment without opening that cellar fridge door for too long.</li>
  <li><b>Safety boxes</b>: It is common for people to forget exactly which valuables they have stored in their safety boxes or bank safety deposit boxes.• Moving boxes: It is always a good idea to record in detail the contents of each box when you move.</li>
  <li class="dot"><b>Audio, video, data, and removable media:</b> Keeping track of the content and storage location of removable media can be a hassle. A system like ours can really help to make that task a breeze.</li>
  <li class="dot"><b>Keys</b>: In a situation such a property management, you can keep track of hundreds of keys for every property you manage. Using Lumo-Pathe will easily organize your key boxes without losing track of where the keys for each property are located.</li>
</ul>

<section class="why-brand"></section>
<h2 class="brand-title" style="color:var(--white)">Why Lumo-Pathe?</h2>
<ul class="perks" style="color:var(--white)">
  <li><svg width="26" height="26" viewBox="0 0 24 24"><path fill="var(--star)" d="M12 1l3.1 7.3 7.9.6-6 5.2 1.9 7.7L12 17.6 5.1 21.8 7 14.1 1 8.9l7.9-.6z"/></svg>It is extremely easy to use.</li>
  <li><svg width="26" height="26" viewBox="0 0 24 24"><path fill="var(--star)" d="M12 1l3.1 7.3 7.9.6-6 5.2 1.9 7.7L12 17.6 5.1 21.8 7 14.1 1 8.9l7.9-.6z"/></svg>It Adapts to your stile.</li>
  <li><svg width="26" height="26" viewBox="0 0 24 24"><path fill="var(--star)" d="M12 1l3.1 7.3 7.9.6-6 5.2 1.9 7.7L12 17.6 5.1 21.8 7 14.1 1 8.9l7.9-.6z"/></svg>It’s very affordable. Checkout our pricing plans!</li>
  <li><svg width="26" height="26" viewBox="0 0 24 24"><path fill="var(--star)" d="M12 1l3.1 7.3 7.9.6-6 5.2 1.9 7.7L12 17.6 5.1 21.8 7 14.1 1 8.9l7.9-.6z"/></svg>your data is available almost anywhere in the world.</li>
  <li><svg width="26" height="26" viewBox="0 0 24 24"><path fill="var(--star)" d="M12 1l3.1 7.3 7.9.6-6 5.2 1.9 7.7L12 17.6 5.1 21.8 7 14.1 1 8.9l7.9-.6z"/></svg>&nbsp;Data encryption ensures that your information is always</li>
  <li><svg width="26" height="26" viewBox="0 0 24 24"><path fill="var(--star)" d="M12 1l3.1 7.3 7.9.6-6 5.2 1.9 7.7L12 17.6 5.1 21.8 7 14.1 1 8.9l7.9-.6z"/></svg>private, safe, and secure.</li>
</ul>
<div class="btn-trial-light">30 Day Free Trial</div>

</body>
</html>
```